Additional Technology ICONS for Web project

We have a group of ICONS from one part of the business, and we need some new ICONS generated for other components. We are a telecommunications company with a web portal, and we have ICONS for our hosting products, but not data or voice services.

We require, in the existing ICON Format, a graphic which represents the following:

The Data LOB groups are:
- IP/VPN (e.g. point to point arrow connections)
- Internet
- Voice Services (Telephone)
- Management (control/hands)
- Other (can use same as Hosting)

For voice:
- ISDN (PABX Like)
- PSTN (Telephone Like)
- Inbound (lots of telephones making calls in)

For mobiles:
- Voice (a Mobile)
- Data (Mobile Data) (Phone with Network connection)

The time is set to 2 days, as we are short of time, but I may extend a day to Monday.

Reason: Hi, Some very good designs here, but I need to extend to Monday, so I can give feedback to everyone.

Target Market(s)

Corporate/Business.

Industry/Entity Type

Telecommunications

Requirements
Must have
• The Colour, Circle Style must be the same as the existing hosting icons (see attached full sample, as well as the exact ICONS at the bottom). Only the graphic is the circle needs to change.

example format is to be: Each ICON in the complete blue square background, and darkblue circle/white inside graphic (e.g the cloud) with Text for the demo.

The final delivery needs to be: Each ICON witth the Blue (not selected) and a SECOND ICON INVERTED (Selected) format. No Text, similiar to the attached.
Nice to have
• simple, clean graphics
Should not have
• any other colours.

```html
<!DOCTYPE html>
<html lang="en">
<head>
<meta charset="utf-8">
<title>Service Icons – Hosting, Data, Voice, Mobile</title>
<link href="https://fonts.googleapis.com/css2?family=Arimo:wght@400;700&display=swap" rel="stylesheet">
<style>
  :root {
    --canvas: #ffffff;
    --header: #5b9bd5;
    --header-text: #ffffff;
    --panel: #bcd6ef;
    --panel-fade: #e6f0fa;
    --divider: #ffffff;
    --circle: #1d5fa3;
    --circle-ring: #7fb0e0;
    --sample: #5d92d3;
    --label: #2a5c94;
    --selected: #ffffff;
  }
  * { box-sizing: border-box; margin: 0; padding: 0; }
  html, body { width: 1200px; height: 628px; overflow: hidden; background: var(--canvas); }
  body { font-family: "Arimo", Arial, sans-serif; position: relative; }

  .column-header {
    position: absolute; top: 46px; height: 40px;
    background: var(--header); color: var(--header-text);
    font-size: 18px; display: flex; align-items: center; justify-content: center;
    box-shadow: 1px 1px 2px rgba(0,0,0,.25);
  }
  .column-header.hosting { left: 74px; width: 222px; }
  .column-header.data    { left: 331px; width: 187px; }
  .column-header.voice   { left: 627px; width: 219px; }
  .column-header.mobile  { left: 925px; width: 222px; }

  .menu {
    position: absolute; list-style: none;
    background: linear-gradient(to right, var(--panel) 78%, var(--panel-fade));
  }
  .menu.hosting { left: 108px; top: 99px; width: 137px; }
  .menu.data    { left: 359px; top: 109px; width: 162px; }
  .menu.voice   { left: 654px; top: 109px; width: 162px; }
  .menu.mobile  { left: 948px; top: 109px; width: 166px; }

  .menu-item {
    position: relative; height: 56px; display: flex; align-items: center;
    padding-left: 12px; gap: 12px;
    border-bottom: 2px solid var(--divider);
    font-size: 13px; color: var(--label);
  }
  .menu-item:last-child { border-bottom: none; }
  .menu-item.selected { background: var(--selected); }
  .menu-item.underlined .label { text-decoration: underline; }

  .connector { position: absolute; left: 30px; width: 4px; background: var(--circle); }
  .menu.hosting .connector { top: 28px; height: 280px; }
  .menu.data .connector { top: 28px; height: 112px; }

  .badge {
    position: relative; z-index: 1; width: 36px; height: 36px; border-radius: 50%;
    background: var(--circle); border: 2px solid var(--circle-ring);
    display: flex; align-items: center; justify-content: center; flex: none;
  }
  .badge svg { width: 20px; height: 20px; }
  .plain-glyph { width: 36px; display: flex; justify-content: center; flex: none; position: relative; z-index: 1; }
  .plain-glyph svg { width: 24px; height: 24px; }
  .menu-item.selected .plain-glyph { background: var(--selected); padding: 4px 0; }

  .sample-icon {
    position: absolute; left: 52px; width: 42px; height: 42px; border-radius: 50%;
    background: var(--sample); display: flex; align-items: center; justify-content: center;
  }
  .sample-icon svg { width: 24px; height: 24px; }

  .glyph { fill: none; stroke: #fff; stroke-width: 2; stroke-linecap: round; stroke-linejoin: round; }
  .glyph .solid { fill: #fff; stroke: none; }
  .dark .glyph { stroke: var(--circle); }
  .dark .glyph .solid { fill: var(--circle); }
</style>
</head>
<body>
<svg width="0" height="0" style="position:absolute" aria-hidden="true">
  <symbol id="i-globe" viewBox="0 0 24 24"><g class="glyph"><circle cx="12" cy="12" r="9"/><path d="M3 12h18M12 3c3 3 3 15 0 18M12 3c-3 3-3 15 0 18"/></g></symbol>
  <symbol id="i-network" viewBox="0 0 24 24"><g class="glyph"><rect x="4" y="4" width="16" height="8"/><path d="M6 16h12M8 20h8M12 12v8"/></g></symbol>
  <symbol id="i-monitor" viewBox="0 0 24 24"><g class="glyph"><rect x="3" y="5" width="18" height="11"/><path d="M9 20h6M12 16v4"/></g></symbol>
  <symbol id="i-storage" viewBox="0 0 24 24"><g class="glyph"><rect x="4" y="4" width="16" height="5"/><rect x="4" y="10" width="16" height="5"/><rect x="4" y="16" width="16" height="4"/></g></symbol>
  <symbol id="i-rack" viewBox="0 0 24 24"><g class="glyph"><rect x="5" y="3" width="14" height="18"/><path d="M8 7h8M8 11h8M8 15h8"/></g></symbol>
  <symbol id="i-other" viewBox="0 0 24 24"><g class="glyph"><circle class="solid" cx="6" cy="12" r="2"/><circle class="solid" cx="12" cy="12" r="2"/><circle class="solid" cx="18" cy="12" r="2"/></g></symbol>
  <symbol id="i-case" viewBox="0 0 24 24"><g class="glyph"><rect x="3" y="8" width="18" height="12" rx="1"/><path d="M9 8V5h6v3"/></g></symbol>
  <symbol id="i-vpn" viewBox="0 0 24 24"><g class="glyph"><circle class="solid" cx="4" cy="12" r="2.5"/><circle class="solid" cx="20" cy="12" r="2.5"/><path d="M7 12h10M14 9l3 3-3 3M10 9l-3 3 3 3"/></g></symbol>
  <symbol id="i-people" viewBox="0 0 24 24"><g class="glyph"><circle cx="7" cy="8" r="2.5"/><circle cx="17" cy="8" r="2.5"/><circle cx="12" cy="10" r="2.5"/><path d="M3 18c0-3 2-5 4-5M21 18c0-3-2-5-4-5M7 19c0-3 2-5 5-5s5 2 5 5"/></g></symbol>
  <symbol id="i-handset" viewBox="0 0 24 24"><g class="glyph"><path d="M5 4h4l2 5-2.5 1.5a11 11 0 0 0 5 5L15 13l5 2v4a1 1 0 0 1-1 1A16 16 0 0 1 4 5a1 1 0 0 1 1-1z"/></g></symbol>
  <symbol id="i-pabx" viewBox="0 0 24 24"><g class="glyph"><rect x="5" y="3" width="14" height="6"/><path d="M12 9v4M5 13h14M5 13v4M12 13v4M19 13v4"/><rect x="3" y="17" width="4" height="3"/><rect x="10" y="17" width="4" height="3"/><rect x="17" y="17" width="4" height="3"/></g></symbol>
  <symbol id="i-deskphone" viewBox="0 0 24 24"><g class="glyph"><rect x="4" y="9" width="16" height="11" rx="1"/><path d="M6 9V5h12v4"/><path d="M9 13h2M13 13h2M9 16h2M13 16h2"/></g></symbol>
  <symbol id="i-inbound" viewBox="0 0 24 24"><g class="glyph"><rect x="7" y="4" width="10" height="16" rx="1"/><path d="M10 8h4M10 12h4M10 16h4"/></g></symbol>
  <symbol id="i-mobile" viewBox="0 0 24 24"><g class="glyph"><rect x="8" y="3" width="8" height="18" rx="1.5" transform="rotate(-35 12 12)"/></g></symbol>
  <symbol id="i-mobile-data" viewBox="0 0 24 24"><g class="glyph"><rect x="4" y="7" width="16" height="10" rx="1"/><path d="M7 10h10"/></g></symbol>
</svg>

<div class="sample-icon" style="top:111px"><svg><use href="#i-globe"/></svg></div>
<div class="sample-icon" style="top:164px"><svg><use href="#i-network"/></svg></div>
<div class="sample-icon" style="top:221px"><svg><use href="#i-monitor"/></svg></div>
<div class="sample-icon" style="top:277px"><svg><use href="#i-network"/></svg></div>
<div class="sample-icon" style="top:384px"><svg><use href="#i-case"/></svg></div>

<h2 class="column-header hosting">Hosting</h2>
<h2 class="column-header data">Data</h2>
<h2 class="column-header voice">Voice</h2>
<h2 class="column-header mobile">Mobile</h2>

<ul class="menu hosting">
  <li class="connector"></li>
  <li class="menu-item"><span class="badge"><svg><use href="#i-globe"/></svg></span><span class="label">Internet</span></li>
  <li class="menu-item"><span class="badge"><svg><use href="#i-network"/></svg></span><span class="label">Network</span></li>
  <li class="menu-item selected"><span class="plain-glyph dark"><svg><use href="#i-monitor"/></svg></span><span class="label">Compute</span></li>
  <li class="menu-item"><span class="badge"><svg><use href="#i-storage"/></svg></span><span class="label">Storage</span></li>
  <li class="menu-item underlined"><span class="badge"><svg><use href="#i-rack"/></svg></span><span class="label">Co-location</span></li>
  <li class="menu-item"><span class="badge"><svg><use href="#i-other"/></svg></span><span class="label">Other</span></li>
</ul>

<ul class="menu data">
  <li class="connector"></li>
  <li class="menu-item"><span class="badge"><svg><use href="#i-globe"/></svg></span><span class="label">Internet</span></li>
  <li class="menu-item"><span class="badge"><svg><use href="#i-vpn"/></svg></span><span class="label">IP/VPN</span></li>
  <li class="menu-item selected"><span class="badge"><svg><use href="#i-people"/></svg></span><span class="label">Management</span></li>
  <li class="menu-item"><span class="badge"><svg><use href="#i-handset"/></svg></span><span class="label">Voice Services</span></li>
  <li class="menu-item"><span class="badge"><svg><use href="#i-case"/></svg></span><span class="label">Other</span></li>
</ul>

<ul class="menu voice">
  <li class="menu-item"><span class="badge"><svg><use href="#i-pabx"/></svg></span><span class="label">ISDN</span></li>
  <li class="menu-item"><span class="badge"><svg><use href="#i-handset"/></svg></span><span class="label">PSTN</span></li>
  <li class="menu-item selected"><span class="badge"><svg><use href="#i-inbound"/></svg></span><span class="label">Inbound</span></li>
  <li class="menu-item"><span class="badge"><svg><use href="#i-deskphone"/></svg></span><span class="label">Other</span></li>
</ul>

<ul class="menu mobile">
  <li class="menu-item"><span class="badge"><svg><use href="#i-mobile"/></svg></span><span class="label">Voice</span></li>
  <li class="menu-item"><span class="badge"><svg><use href="#i-mobile-data"/></svg></span><span class="label">Data</span></li>
  <li class="menu-item selected"><span class="badge"><svg><use href="#i-case"/></svg></span><span class="label">Other</span></li>
</ul>
</body>
</html>
```